Corporate Business Card

Very professional, Modern, Not to busy, include phone address email, website
(555) 317-4860, 18716 52nd Avenue S, Kent, WA 98417, marcus@bralvintrust.example, vendrikworks.example

Target Market(s)

Manufacturing

Industry/Entity Type

Aero, machining, manufacturing, Off road racing

Contact Information for Business Card

Phone, address email, website

```html
<!DOCTYPE html>
<html lang="en">
<head>
<meta charset="utf-8">
<title>Vendrik Works – Business Card</title>
<link rel="stylesheet" href="https://fonts.googleapis.com/css2?family=Montserrat:wght@400;500;700&display=swap">
<style>
  :root {
    --navy: #17356f;
    --red: #d2232a;
    --white: #ffffff;
    --ink: #1d1d1f;
    --backdrop: #4a4a4a;
  }
  * { margin: 0; padding: 0; box-sizing: border-box; }
  html, body { width: 1200px; height: 801px; overflow: hidden; }
  body {
    background: var(--backdrop);
    font-family: "Montserrat", Arial, sans-serif;
    display: flex;
    align-items: center;
    justify-content: center;
    gap: 40px;
  }
  .card {
    position: relative;
    width: 540px;
    height: 309px;
    overflow: hidden;
  }
  .card-front { background: var(--white); }
  .card-back { background: var(--navy); }

  .edge-band { position: absolute; inset: 0; }

  .brand {
    position: absolute;
    display: flex;
    align-items: center;
    gap: 8px;
    font-weight: 700;
    letter-spacing: 0.3px;
    white-space: nowrap;
  }
  .brand-mark { width: 9px; height: 9px; background: var(--red); flex: none; }
  .card-front .brand { left: 40px; top: 130px; font-size: 22px; color: var(--navy); }
  .card-front .brand-rule {
    position: absolute; left: 40px; top: 168px; width: 190px; height: 1.5px;
    background: var(--navy);
  }
  .divider {
    position: absolute; left: 272px; top: 58px; width: 1.5px; height: 190px;
    background: var(--red);
  }
  .contact {
    position: absolute; left: 292px; top: 40px;
    color: var(--ink); font-size: 11px; line-height: 1.45;
  }
  .contact-name { color: var(--red); font-weight: 700; font-size: 17px; letter-spacing: 0.3px; line-height: 1.2; }
  .contact-title { margin-bottom: 12px; }
  .contact-address { margin-bottom: 12px; }
  .contact-line { display: flex; align-items: center; gap: 6px; }
  .contact-line svg { width: 10px; height: 10px; flex: none; }

  .card-back .brand { left: 82px; top: 112px; font-size: 46px; color: var(--white); gap: 14px; }
  .card-back .brand-mark { width: 18px; height: 18px; }
  .card-back .brand-rule {
    position: absolute; left: 60px; top: 196px; width: 260px; height: 2px;
    background: var(--white);
  }
</style>
</head>
<body>
  <section class="card card-front">
    <svg class="edge-band" viewBox="0 0 540 309" aria-hidden="true">
      <polygon points="40,309 318,250 318,309" fill="var(--navy)"/>
      <polygon points="326,248 540,203 540,232 326,278" fill="var(--red)"/>
    </svg>
    <div class="brand"><span class="brand-mark"></span>Vendrik Works</div>
    <div class="brand-rule"></div>
    <div class="divider"></div>
    <div class="contact">
      <div class="contact-name">MARCUS HALVARD</div>
      <div class="contact-title">Owner/CEO</div>
      <div class="contact-address">4107, 18716 52nd<br>Avenue S, Kent, WA 98417</div>
      <div class="contact-line">
        <svg viewBox="0 0 10 10"><path d="M2 0.5 L3.8 2.6 L2.9 3.7 Q4.2 6 6.3 7.1 L7.4 6.2 L9.5 8 L8.2 9.5 Q3.5 9 0.5 1.8 Z" fill="var(--red)"/></svg>
        <span>(555) 317-4860</span>
      </div>
      <div class="contact-line">
        <svg viewBox="0 0 10 10"><rect x="0.5" y="2" width="9" height="6.5" fill="var(--red)"/><path d="M0.5 2 L5 5.8 L9.5 2" stroke="var(--white)" stroke-width="0.9" fill="none"/></svg>
        <span>marcus@bralvintrust.example</span>
      </div>
      <div class="contact-line">
        <svg viewBox="0 0 10 10"><circle cx="5" cy="5" r="4.5" fill="var(--red)"/><path d="M0.5 5 H9.5 M5 0.5 Q2.5 5 5 9.5 M5 0.5 Q7.5 5 5 9.5" stroke="var(--white)" stroke-width="0.7" fill="none"/></svg>
        <span>www.vendrikworks.example</span>
      </div>
    </div>
  </section>

  <section class="card card-back">
    <div class="brand"><span class="brand-mark"></span>Vendrik Works</div>
    <div class="brand-rule"></div>
  </section>
</body>
</html>
```